Sports hypnotherapist needs electronic letterhead design

Need a simple but classy design for a letterhead that looks good when printed. Its for a hypnotherapist who specialises in elite sport. Should have my company name and address and website details on it. I specialise in footballers.
Should look good electronically and when printed.
Include all contact details as shown in the must haves.

Target Market(s)

Sports people, elite sport.

Industry/Entity Type

Hypnotherapy

Font styles to use
Sans Serif

Colors

Designer to choose colors to be used in the design.

Requirements
Must have
• NEEDS TO BE DESIGNED IN MS WORD
• Logo +
• Tidewell Focus Hypnotherapists
• 27 Harrowmere Close
• Bracknell
• RG19 4TX
• Tel: 07700 900461
• E: tidewellfocuscoaching@quorvex.co.uk
• www: http://www.tidewell-focus.co.uk.
• Dorian Lacey
• Clinical hypnotherapist, hypnoanalyst, mental resilience coach, MSc, Dip PHH
Nice to have
• A watermark?
• Plenty of space for the A4 letter
• Prints well.
Should not have
• Too much clutter.
• Too much colour that will be costly to print.

```html
<!DOCTYPE html>
<html lang="en">
<head>
<meta charset="utf-8">
<title>Tidewell Focus Hypnotherapists – Letterhead</title>
<link rel="stylesheet" href="https://fonts.googleapis.com/css2?family=Open+Sans:wght@400;600;700&display=swap">
<style>
  :root {
    --backdrop: #b9b9b9;
    --paper: #f4f4f4;
    --ink: #1a1a1a;
    --muted: #2e2e2e;
    --accent: #1fa3d8;
    --rule: #3a3a3a;
    --watermark-a: #dedede;
    --watermark-b: #e3e9ec;
  }
  * { box-sizing: border-box; margin: 0; padding: 0; }
  html, body {
    width: 1200px; height: 780px; overflow: hidden;
    background: var(--backdrop);
    font-family: "Open Sans", Arial, sans-serif;
  }
  .letterhead {
    position: absolute; left: 338px; top: 20px;
    width: 524px; height: 740px;
    background: var(--paper);
  }
  .brand {
    position: absolute; left: 42px; top: 56px;
    display: flex; align-items: center; gap: 7px;
  }
  .brand-dot {
    width: 14px; height: 14px; border-radius: 50%;
    background: var(--accent);
  }
  .brand-name {
    font-weight: 700; font-size: 19px; color: var(--ink);
    letter-spacing: -0.3px; line-height: 1;
  }
  .watermark {
    position: absolute; left: 134px; top: 121px;
    width: 312px; height: 467px;
  }
  .signature-block {
    position: absolute; left: 206px; top: 648px; width: 287px;
  }
  .person-name {
    font-weight: 700; font-size: 9px; color: var(--accent);
  }
  .person-title {
    font-size: 7.6px; color: var(--muted); margin-top: 1px;
    padding-bottom: 4px; border-bottom: 1px solid var(--rule);
    white-space: nowrap;
  }
  .contact {
    display: flex; margin-top: 6px;
    font-size: 7.6px; color: var(--muted); line-height: 11px;
  }
  .contact-address { width: 113px; }
  .contact-lines { list-style: none; }
  .contact-lines li { display: flex; align-items: center; gap: 4px; white-space: nowrap; }
  .contact-lines svg { width: 6px; height: 6px; fill: var(--accent); flex: none; }
</style>
</head>
<body>
  <main class="letterhead">
    <header class="brand">
      <span class="brand-dot"></span>
      <span class="brand-name">Tidewell Focus</span>
    </header>

    <svg class="watermark" role="img" aria-label="Faint watermark area for a standing figure and a sprinting athlete" viewBox="0 0 312 467">
      <defs>
        <linearGradient id="watermarkFade" x1="0" y1="0" x2="1" y2="0">
          <stop offset="0" stop-color="var(--paper)"/>
          <stop offset="0.35" stop-color="var(--watermark-a)"/>
          <stop offset="0.7" stop-color="var(--watermark-b)"/>
          <stop offset="1" stop-color="var(--paper)"/>
        </linearGradient>
      </defs>
      <rect width="312" height="467" rx="30" fill="url(#watermarkFade)" opacity="0.6"/>
    </svg>

    <footer class="signature-block">
      <p class="person-name">Dorian Lacey</p>
      <p class="person-title">Clinical hypnotherapist, hypnoanalyst, mental resilience coach, MSc, Dip PHH</p>
      <div class="contact">
        <address class="contact-address" style="font-style:normal">27 Harrowmere Close, Bracknell<br>RG19 4TX</address>
        <ul class="contact-lines">
          <li><svg viewBox="0 0 10 10"><path d="M2 0.5 L4 2.5 L3 4 Q4.5 6 6 7 L7.5 6 L9.5 8 L8 9.6 Q3.5 9 0.4 2 Z"/></svg>07700 900461</li>
          <li><svg viewBox="0 0 10 10"><path d="M0 2 H10 V8.5 H0 Z M0.8 2.6 L5 5.8 L9.2 2.6" stroke="#f4f4f4" stroke-width="0.8"/></svg>tidewellfocuscoaching@quorvex.co.uk</li>
          <li><svg viewBox="0 0 10 10"><circle cx="5" cy="5" r="4.6"/><path d="M0.6 5 H9.4 M5 0.5 Q2 5 5 9.5 Q8 5 5 0.5" stroke="#f4f4f4" stroke-width="0.7" fill="none"/></svg>www.tidewell-focus.co.uk.</li>
        </ul>
      </div>
    </footer>
  </main>
</body>
</html>
```